Travel Itinerary Planning Website Redesign

We have built our own website for a travel itinerary planning service using Wix but are not professional designers. We need help getting over the finish line with a redesign of our website. <br/><br/>We like material design elements, icons and styling. The pages need to flow well one to another and evoke a sense of exclusivity, without giving the impression that it's unattainable. The website doesn't need to keep its current "boxy" format but instead should have a better aesthetic and flow. We're also looking for a complete redesign of the "How It Works" section (shown on two different pages of the website) to be more visually pleasing and easy to understand (maybe using icons or infographic style people). <br/><br/>We already have our logo and selected colors. The copy is also available on the live site as well. The redesign will focus on 4 pages: the homepage and the three service pages (one page per service). The website is currently live at www.trelmavista.com. Fonts should be Helvetica Bold, Regular and Light. Preferred color scheme is attached.

Target Market(s)

Ages 28-65, living in the US, mostly large cities with a desire for well planned, non-group travels

Industry/Entity Type

Travel Industry

Font styles to use
Other font styles liked:
• Helvetica

Colors

Designer to choose colors to be used in the design.

Requirements
Must have
• Make sure to use colors we provided in the attachment and what's on the current website
• Redesign "How it Works"
• Include ambassadors area
• Have a second page that showcases how the "Personal Trip Planning" page should look
Should not have
• No header menu needed for this project

```html
<!DOCTYPE html>
<html lang="en">
<head>
<meta charset="utf-8">
<title>Trelmavista — Handcrafted Travel Itineraries</title>
<link href="https://fonts.googleapis.com/css2?family=Inter:wght@300;400;700&display=swap" rel="stylesheet">
<style>
:root{
  --gold:#f8c56a;
  --gold-deep:#d9a74d;
  --brown:#6e5433;
  --brown-dark:#3d2b17;
  --tan:#a98c68;
  --ink:#2a2a2a;
  --grey:#8a8a8a;
  --footer:#1f1e1d;
  --white:#ffffff;
}
*{box-sizing:border-box;margin:0;padding:0}
html,body{width:1200px;height:4745px;overflow:hidden}
body{font-family:"Inter",Helvetica,Arial,sans-serif;color:var(--ink);background:var(--white);position:relative}
section,footer{position:absolute;left:0;width:1200px;overflow:hidden}
.abs{position:absolute}
.center{left:0;width:1200px;text-align:center}
.pill{position:absolute;display:flex;align-items:center;justify-content:center;border-radius:20px;font-weight:700;font-size:10px;letter-spacing:.6px;text-transform:uppercase}
.pill-gold{background:var(--gold);color:var(--brown-dark)}
.pill-brown{background:var(--brown);color:var(--white)}

/* hero */
.hero{top:0;height:600px;background:linear-gradient(180deg,#8b9196 0%,#5d6a5e 30%,#3f4a36 60%,#4f4a36 100%)}
.hero-shade{position:absolute;inset:0;background:linear-gradient(180deg,rgba(0,0,0,.05),rgba(0,0,0,.35))}
.brand{position:absolute;left:92px;top:28px;display:flex;flex-direction:column;align-items:center;gap:8px}
.brand-dot{width:58px;height:58px;border-radius:50%;background:var(--gold)}
.brand-name{font-weight:700;font-size:11px;color:var(--gold);letter-spacing:.5px}
.hero h1{position:absolute;top:246px;font-weight:700;color:var(--white);line-height:1.1}
.hero h1 .small{display:block;font-size:30px}
.hero h1 .big{display:block;font-size:44px;margin-top:6px}
.hero-sub{top:338px;font-size:16px;color:var(--white);font-weight:300}

/* services */
.services{top:600px;height:607px;background:linear-gradient(180deg,#d9a957 0%,#c99a4f 55%,#d6a552 100%)}
.service-card{position:absolute;top:267px;width:316px;height:257px;background:var(--white);text-align:center;padding:76px 34px 0}
.service-photo{position:absolute;top:83px;width:232px;height:232px;border-radius:50%;border:4px solid var(--white)}
.service-card h3{font-weight:400;font-size:22px;color:var(--ink)}
.service-card p{margin-top:18px;font-size:12px;line-height:21px;color:var(--grey);font-weight:300}
.service-card .pill{left:99px;top:200px;width:118px;height:30px}

/* how it works */
.how{top:1207px;height:403px;background:var(--white)}
.how h2{top:60px;font-size:36px;font-weight:700;color:#333}
.step{position:absolute;top:155px;width:170px;height:180px}
.step-diamond{position:absolute;left:25px;top:20px;width:122px;height:122px;border-radius:16px;transform:rotate(45deg)}
.step-label{position:absolute;left:0;top:72px;width:170px;text-align:center;font-size:14px;line-height:20px;color:var(--white)}
.step-icon{position:absolute;left:67px;top:30px}
.step-num{position:absolute;left:60px;top:119px;width:50px;height:50px;border-radius:50%;display:flex;align-items:center;justify-content:center;font-size:20px;font-weight:700;color:var(--white)}

/* why */
.why{top:1610px;height:449px;background:linear-gradient(180deg,#7a4f28 0%,#8a5a2e 40%,#5e3a1c 100%)}
.why h2{top:38px;font-size:36px;font-weight:700;color:var(--white)}
.why-highlight{position:absolute;left:602px;top:120px;width:252px;height:281px;background:rgba(255,255,255,.08)}
.why-item{position:absolute;top:152px;width:220px;color:var(--white)}
.why-icon{width:98px;height:74px;border-radius:38px;background:var(--white);display:flex;align-items:center;justify-content:center}
.why-item h4{margin-top:26px;font-size:16px;font-weight:400;line-height:22px}
.why-item p{margin-top:16px;font-size:12px;line-height:19px;color:rgba(255,255,255,.82);font-weight:300}

/* ambassadors */
.ambassadors{top:2059px;height:549px;background:var(--white)}
.amb-kicker{top:69px;font-size:20px;color:#333}
.amb-title{top:110px;font-size:36px;font-weight:700;color:#333}
.amb{position:absolute;top:200px;width:300px;text-align:center}
.amb svg{display:block;margin:0 auto}
.amb h4{margin-top:40px;font-size:22px;font-weight:700;color:#333}
.amb p{margin-top:6px;font-size:12px;color:var(--grey)}
.amb-arrow{position:absolute;top:322px}

/* cta */
.cta{top:2608px;height:218px;background:linear-gradient(180deg,#4a2a16 0%,#8c4a22 45%,#b0683a 75%,#6b3a1c 100%)}
.cta h2{top:64px;font-size:34px;font-weight:700;color:var(--white)}
.cta .pill{left:535px;top:121px;width:130px;height:32px}

/* resources */
.resources{top:2826px;height:1476px;background:var(--white)}
.res-kicker{top:68px;font-size:20px;color:#333}
.res-title{top:108px;font-size:36px;font-weight:700;color:#333}
.guide{position:absolute;width:580px}
.guide .updated{font-size:13px;line-height:16px;color:var(--grey)}
.guide h3{margin-top:12px;font-size:22px;line-height:26px;font-weight:700;color:#222}
.guide .subtitle{margin-top:0;font-size:14px;line-height:18px;color:#333}
.guide p{margin-top:8px;font-size:12px;line-height:22px;color:var(--grey);font-weight:300}
.guide h3 + p,.guide .subtitle + p{margin-top:10px}
.guide .pill{position:relative;margin-top:20px;width:118px;height:32px}
.trail{position:absolute;left:0;top:0}

/* footer */
.site-footer{top:4302px;height:443px;background:var(--footer);color:#b5b5b5}
.foot-head{position:absolute;top:58px;font-size:17px;font-weight:700;color:var(--gold-deep)}
.foot-text{position:absolute;left:94px;top:100px;width:270px;font-size:11px;line-height:19px}
.foot-brand{position:absolute;left:96px;top:180px;display:flex;flex-direction:column;align-items:center;gap:6px}
.foot-brand .brand-dot{width:44px;height:44px}
.foot-links{position:absolute;left:442px;top:98px;list-style:none;font-size:11px}
.foot-links li{height:30px}
.foot-links li::before{content:"\2192";margin-right:8px;color:#ddd}
.field{position:absolute;background:var(--white);color:#555;font-size:9px;padding:6px 8px}
.submit{position:absolute;left:1019px;top:214px;width:87px;height:28px;border-radius:14px;background:var(--gold);color:var(--brown-dark);font-size:10px;font-weight:700;display:flex;align-items:center;justify-content:center}
.social{position:absolute;top:305px;left:569px;display:flex;gap:10px}
.social span{width:24px;height:24px;border-radius:50%;background:var(--white)}
.copyright{position:absolute;top:348px;left:0;width:1200px;text-align:center;font-size:9px;line-height:16px;color:#8f8f8f}
.copyright b{color:var(--gold-deep);font-weight:400}
</style>
</head>
<body>

<section class="hero">
  <div class="abs" style="inset:0" role="img" aria-label="Photo of a mountain citadel among green Andean peaks"></div>
  <div class="hero-shade"></div>
  <div class="brand"><span class="brand-dot"></span><span class="brand-name">TRELMAVISTA</span></div>
  <h1 class="center"><span class="small">UNLOCK ALL THE</span><span class="big">POSSIBILITIES OF THE JOURNEY AHEAD</span></h1>
  <p class="abs center hero-sub">Trelmavista creates template-free, handcrafted travel itineraries just for you.</p>
  <a class="pill pill-gold" style="left:535px;top:385px;width:130px;height:32px">Get Started</a>
</section>

<section class="services">
  <div class="abs" style="inset:0;background:radial-gradient(ellipse at 50% 30%,rgba(255,220,150,.35),transparent 60%)" role="img" aria-label="Warm sepia photo of travellers with raised arms at sunset"></div>

  <div class="service-card" style="left:94px">
    <h3>PERSONAL TRIP</h3>
    <p>Get your personalized itinerary from an expert travel engineer and access it anywhere.</p>
    <a class="pill pill-brown">Learn More</a>
  </div>
  <div class="service-photo" style="left:136px;background:linear-gradient(160deg,#9fb7b0,#6f8a86 55%,#4a4a42)" role="img" aria-label="Photo of a traveller watching hot air balloons over rock valleys"></div>

  <div class="service-card" style="left:442px">
    <h3>BUSINESS TRIP</h3>
    <p>Get a tailored sightseeing itinerary while on-the-go for business.</p>
    <a class="pill pill-brown">Learn More</a>
  </div>
  <div class="service-photo" style="left:484px;background:linear-gradient(160deg,#b7c0c6,#7f8890 50%,#3a3a3e)" role="img" aria-label="Photo of a businessman with a rolling suitcase on a city street"></div>

  <div class="service-card" style="left:789px">
    <h3>OVERSEAS EVENT</h3>
    <p>Get recommendations and logistics guidance for your overseas events.</p>
    <a class="pill pill-brown">Learn More</a>
  </div>
  <div class="service-photo" style="left:831px;background:linear-gradient(160deg,#d94a8a,#8a2a5a 55%,#3a1a3a)" role="img" aria-label="Photo of friends in masks celebrating at a party"></div>
</section>

<section class="how">
  <h2 class="abs center">HOW IT WORKS</h2>

  <div class="step" style="left:191px">
    <div class="step-diamond" style="background:var(--gold)"></div>
    <svg class="step-icon" width="36" height="36" viewBox="0 0 36 36" fill="none" stroke="#3d2b17" stroke-width="2"><circle cx="18" cy="9" r="5"/><path d="M4 28c4-6 10-6 14-3h10l4-3M4 32h26"/></svg>
    <div class="step-label" style="color:var(--brown-dark)">Select<br>The Service</div>
    <div class="step-num" style="background:var(--gold-deep)">1</div>
  </div>

  <div class="step" style="left:362px">
    <div class="step-diamond" style="background:var(--brown)"></div>
    <svg class="step-icon" width="36" height="36" viewBox="0 0 36 36" fill="none" stroke="#fff" stroke-width="2"><rect x="7" y="6" width="20" height="26" rx="2"/><path d="M12 14h10M12 20h10M12 26h6"/></svg>
    <div class="step-label">Complete the<br>Survey</div>
    <div class="step-num" style="background:var(--brown-dark)">2</div>
  </div>

  <div class="step" style="left:522px">
    <div class="step-diamond" style="background:#c79c52"></div>
    <svg class="step-icon" width="36" height="36" viewBox="0 0 36 36" fill="none" stroke="#fff" stroke-width="2"><path d="M18 32s-9-10-9-17a9 9 0 0 1 18 0c0 7-9 17-9 17z"/><circle cx="18" cy="15" r="3"/></svg>
    <div class="step-label">Connect with a<br>Travel Engineer</div>
    <div class="step-num" style="background:var(--brown)">3</div>
  </div>

  <div class="step" style="left:679px">
    <div class="step-diamond" style="background:var(--tan)"></div>
    <svg class="step-icon" width="36" height="36" viewBox="0 0 36 36" fill="none" stroke="#fff" stroke-width="2"><circle cx="18" cy="13" r="10"/><path d="M13 23l3 6h4l3-6M15 32h6"/></svg>
    <div class="step-label">Access<br>Custom Itinerary</div>
    <div class="step-num" style="background:var(--brown)">4</div>
  </div>

  <div class="step" style="left:822px">
    <div class="step-diamond" style="background:var(--gold)"></div>
    <svg class="step-icon" width="36" height="36" viewBox="0 0 36 36" fill="#3d2b17"><circle cx="12" cy="7" r="4"/><circle cx="24" cy="7" r="4"/><rect x="8" y="13" width="8" height="19" rx="2"/><rect x="20" y="13" width="8" height="19" rx="2"/></svg>
    <div class="step-label" style="color:var(--brown-dark)">Travel<br>Worry-Free</div>
    <div class="step-num" style="background:var(--gold-deep)">5</div>
  </div>
</section>

<section class="why">
  <div class="abs" style="inset:0;background:linear-gradient(180deg,transparent 40%,rgba(40,20,8,.35))" role="img" aria-label="Photo of rolling desert dunes in warm brown light"></div>
  <h2 class="abs center">WHY TRELMAVISTA</h2>
  <div class="why-highlight"></div>

  <div class="why-item" style="left:94px">
    <div class="why-icon"><svg width="44" height="40" viewBox="0 0 44 40" fill="#f5b82e"><path d="M10 2l2 5h5l-4 3 2 5-5-3-5 3 2-5-4-3h5z"/><path d="M30 2l2 5h5l-4 3 2 5-5-3-5 3 2-5-4-3h5z"/><path d="M20 20l2 5h5l-4 3 2 5-5-3-5 3 2-5-4-3h5z"/></svg></div>
    <h4>5-Star Travel Planning for Every Budget</h4>
    <p>White-glove service and exceptional travel planning is our motto.</p>
  </div>

  <div class="why-item" style="left:351px">
    <div class="why-icon"><svg width="40" height="36" viewBox="0 0 40 36"><rect x="4" y="9" width="32" height="24" rx="3" fill="#d94a3a"/><rect x="14" y="3" width="12" height="6" rx="2" fill="none" stroke="#3a6ab0" stroke-width="2"/><rect x="10" y="14" width="6" height="14" fill="#3a6ab0"/></svg></div>
    <h4>A Travel Itinerary Engineered Just For You</h4>
    <p>Trelmavista caters to all needs. Using points? Lounge access? No problem. We mastered the art of optimizing miles.</p>
  </div>

  <div class="why-item" style="left:635px">
    <div class="why-icon"><svg width="36" height="40" viewBox="0 0 36 40"><path d="M18 2l15 6v11c0 10-7 16-15 19C10 35 3 29 3 19V8z" fill="#2aa86a"/><path d="M11 20l5 5 9-10" fill="none" stroke="#fff" stroke-width="3"/></svg></div>
    <h4>Avoid Common Traveler Mistakes</h4>
    <p>While planning or vacationing, it is easy to make costly mistakes. Let us remove that worry!</p>
  </div>

  <div class="why-item" style="left:902px">
    <div class="why-icon"><svg width="40" height="36" viewBox="0 0 40 36"><ellipse cx="20" cy="20" rx="14" ry="12" fill="#e84a5f"/><circle cx="20" cy="6" r="4" fill="#2aa8a0"/></svg></div>
    <h4>Save Time and Money</h4>
    <p>A sound travel itinerary takes dedication &amp; commitment, qualities that we provide for each handcrafted journey.</p>
  </div>
</section>

<section class="ambassadors">
  <p class="abs center amb-kicker">EXPERIENCES CURATED WITH INSPIRATION</p>
  <h2 class="abs center amb-title">FROM OUR BRAND AMBASSADORS</h2>

  <svg class="amb-arrow" style="left:82px" width="14" height="22" viewBox="0 0 14 22" fill="none" stroke="#444" stroke-width="2"><path d="M11 2L3 11l8 9"/></svg>
  <svg class="amb-arrow" style="left:1104px" width="14" height="22" viewBox="0 0 14 22" fill="none" stroke="#444" stroke-width="2"><path d="M3 2l8 9-8 9"/></svg>

  <div class="amb" style="left:112px">
    <svg width="206" height="206" viewBox="0 0 206 206" role="img" aria-label="Portrait of a lifestyle influencer in a beret against autumn leaves">
      <defs><linearGradient id="ambA" x1="0" y1="0" x2="1" y2="1"><stop offset="0" stop-color="#c9753a"/><stop offset="1" stop-color="#e8d8c8"/></linearGradient></defs>
      <path d="M40 10C95-5 196 12 204 72c8 60-52 132-114 132C30 204 0 144 5 84 8 44 18 20 40 10z" fill="url(#ambA)"/>
    </svg>
    <h4>MARGAUX DELAINE</h4>
    <p>French Lifestyle Influencer</p>
  </div>

  <div class="amb" style="left:448px">
    <svg width="206" height="206" viewBox="0 0 206 206" role="img" aria-label="Portrait of the founder in front of green foliage">
      <defs><linearGradient id="ambB" x1="0" y1="0" x2="1" y2="1"><stop offset="0" stop-color="#6a8a4a"/><stop offset="1" stop-color="#2c3a24"/></linearGradient></defs>
      <path d="M40 10C95-5 196 12 204 72c8 60-52 132-114 132C30 204 0 144 5 84 8 44 18 20 40 10z" fill="url(#ambB)"/>
    </svg>
    <h4>LUCIEN FAUREL</h4>
    <p>Founder &amp; CEO</p>
  </div>

  <div class="amb" style="left:785px">
    <svg width="206" height="206" viewBox="0 0 206 206" role="img" aria-label="Portrait of a singer with long dark hair against a light wall">
      <defs><linearGradient id="ambC" x1="0" y1="0" x2="1" y2="1"><stop offset="0" stop-color="#e7e0d8"/><stop offset="1" stop-color="#5a3a2a"/></linearGradient></defs>
      <path d="M40 10C95-5 196 12 204 72c8 60-52 132-114 132C30 204 0 144 5 84 8 44 18 20 40 10z" fill="url(#ambC)"/>
    </svg>
    <h4>BIANCA ORSETTI</h4>
    <p>Italian Singer</p>
  </div>
</section>

<section class="cta">
  <div class="abs" style="inset:0" role="img" aria-label="Photo of desert dunes at dusk"></div>
  <h2 class="abs center">READY TO GET PLANNING?</h2>
  <a class="pill pill-gold">View Services</a>
</section>

<section class="resources">
  <svg class="trail" width="1200" height="1476" viewBox="0 0 1200 1476" fill="none" stroke="#8a8a8a" stroke-width="1.5" stroke-dasharray="2 4">
    <path d="M378 68C250 80 130 130 118 220"/>
    <path d="M390 560C460 610 520 630 582 650C640 670 690 690 722 705"/>
    <path d="M770 960C750 1040 700 1080 620 1100C560 1112 500 1115 452 1120"/>
    <path d="M150 1330C140 1360 125 1380 112 1396"/>
  </svg>
  <svg class="trail" width="1200" height="1476" viewBox="0 0 1200 1476" fill="var(--gold)">
    <circle cx="380" cy="68" r="6"/><circle cx="582" cy="650" r="6"/><circle cx="620" cy="1100" r="6"/><circle cx="112" cy="1396" r="6"/>
  </svg>

  <p class="abs center res-kicker">START WITH OUR</p>
  <h2 class="abs center res-title">FREE TRAVEL RESOURCES</h2>

  <svg class="abs" style="left:94px;top:170px" width="388" height="420" viewBox="0 0 388 420" role="img" aria-label="Photo of a pagoda street in Kyoto at dusk with travellers in kimono">
    <defs><linearGradient id="japan" x1="0" y1="0" x2="0" y2="1"><stop offset="0" stop-color="#e8a877"/><stop offset=".5" stop-color="#8a5a48"/><stop offset="1" stop-color="#3a3038"/></linearGradient></defs>
    <path d="M190 4C240 70 388 200 388 292C388 372 300 420 194 420C90 420 0 372 0 292 0 200 140 70 190 4z" fill="url(#japan)"/>
  </svg>
  <div class="guide" style="left:524px;top:271px">
    <p class="updated">Updated: 3 days ago</p>
    <h3>2020 Japan Travel Guide</h3>
    <p>Japan, the land of the rising sun and robotics! What a truly exceptional destination. I must be honest, Japan was not in my top 10 countries to visit, but after experiencing the beauty, peacefulness and excitement from our Nippon adventure, I can say with conviction that Japan deserves a spot in everybody's must-see list!</p>
    <p>Japan is also a land of extreme variations that will awaken your senses in new ways and will, as it does to anyone coming back from Japan, make you miss and cherish those incredible moments.</p>
    <a class="pill pill-brown">Read More</a>
  </div>

  <div class="guide" style="left:94px;top:675px">
    <p class="updated">Updated: 3 days ago</p>
    <h3>2020 Peru Travel Guide:</h3>
    <p class="subtitle">Hiking Machu Picchu (Inca Trail)</p>
    <p>Quintessentially bucolic, Peru attracts foodies, hikers, history-buffs and nature-lovers alike. If you are going to Peru for the first time and are getting overwhelmed by the amount of information out there - welcome to the club!</p>
    <p>Planning my first trip to this fascinating South American gem took time and patience, but in the end, I was able to organize an amazing and budget-friendly trip of a lifetime. We can organize a tailored trip for you as well.</p>
    <a class="pill pill-brown">Read More</a>
  </div>
  <svg class="abs" style="left:721px;top:615px" width="388" height="388" viewBox="0 0 388 388" role="img" aria-label="Photo of a hiker above a turquoise glacial lake beneath snowy peaks">
    <defs><linearGradient id="peru" x1="0" y1="0" x2="0" y2="1"><stop offset="0" stop-color="#4a7ab8"/><stop offset=".35" stop-color="#dfe6ec"/><stop offset=".6" stop-color="#3aa0b0"/><stop offset="1" stop-color="#7a7a72"/></linearGradient></defs>
    <path d="M60 40C150-10 340 0 380 90c26 80-50 240-180 290-80 30-160-30-180-130C0 160 10 70 60 40z" fill="url(#peru)"/>
  </svg>

  <svg class="abs" style="left:94px;top:968px" width="388" height="440" viewBox="0 0 388 440" role="img" aria-label="Photo of the Sphinx and pyramid in Giza with a visitor walking">
    <defs><linearGradient id="egypt" x1="0" y1="0" x2="0" y2="1"><stop offset="0" stop-color="#d8e4ea"/><stop offset=".35" stop-color="#c99a62"/><stop offset="1" stop-color="#e8cfa5"/></linearGradient></defs>
    <path d="M190 4C240 74 388 210 388 306C388 390 300 440 194 440C90 440 0 390 0 306 0 210 140 74 190 4z" fill="url(#egypt)"/>
  </svg>
  <div class="guide" style="left:524px;top:1100px">
    <p class="updated">Updated: 3 days ago</p>
    <h3>2020 Egypt Travel Guide</h3>
    <p>Home to the last of the seven wonders of the ancient world, Egypt is as mysterious as it is breathtaking. With a history that stretches as far back as we have records of, a trip to Egypt seems like a natural desire.</p>
    <p>This Egypt travel guide is designed to answer some of your burning questions, provide tips for traveling and things to do in Egypt, and help you make the most of your trip.</p>
    <a class="pill pill-brown">Read More</a>
  </div>
</section>

<footer class="site-footer">
  <h5 class="foot-head" style="left:94px">COMPANY</h5>
  <p class="foot-text">Trelmavista's mission is to engineer personalized, handcrafted travel itineraries and event plans for travelers worldwide.</p>
  <div class="foot-brand"><span class="brand-dot"></span><span class="brand-name">TRELMAVISTA</span></div>

  <h5 class="foot-head" style="left:442px">ABOUT TRELMAVISTA</h5>
  <ul class="foot-links">
    <li>Personal Trip Planning</li>
    <li>Business Trip Planning</li>
    <li>Overseas Event Planning</li>
    <li>Free Travel Resources</li>
    <li>Terms and Conditions</li>
    <li>Privacy Policy</li>
  </ul>

  <h5 class="foot-head" style="left:738px">GET IN TOUCH</h5>
  <div class="field" style="left:738px;top:105px;width:182px;height:28px">Name:</div>
  <div class="field" style="left:738px;top:138px;width:182px;height:28px">Email:</div>
  <div class="field" style="left:738px;top:171px;width:182px;height:28px">Phone:</div>
  <div class="field" style="left:929px;top:105px;width:177px;height:94px">Message:</div>
  <div class="submit">SUBMIT</div>

  <div class="social"><span></span><span></span></div>
  <p class="copyright">COPYRIGHT © 2020 <b>TRELMAVISTA</b>. ALL RIGHTS RESERVED.<br>Terms and Conditions | Privacy Policy</p>
</footer>

</body>
</html>
```